Grey Heron Estates Inc Business Card design

Grey Heron Estates Inc is a West Vancouver based boutique brokerage specializing in the marketing and sale of luxury and waterfront real estate.

This card is for Marlon Tevaki, Vice-President.

The card should have something modern and unique about. Some sort of gimmick would be nice.

I would like it to use or update the grey heron estates logo visible at www.greyheronestates-example.com

Very open to any design.

Target Market(s)

humans, the type with money

Industry/Entity Type

Marketing

Requirements
Must have
• The name Marlon Tevaki

Company name Grey Heron Estates Inc

Phone 604-512-3047

Fax 604-488-1630

email marlontevaki@mailbox-example.com

website www.marlontevaki-example.com

LOGO

tag line"a fresh approach to real estate in west vancouver"

the attched pic of me if possible
Nice to have
• Something that would make people say "nice card" and not throw it in the garbage immediately, open to ideas
Should not have
• anything that looks like a template

```html
<!DOCTYPE html>
<html lang="en">
<head>
<meta charset="utf-8">
<title>Grey Heron Estates Inc — Business Card</title>
<link href="https://fonts.googleapis.com/css2?family=Tinos:wght@400;700&display=swap" rel="stylesheet">
<style>
  :root {
    --stage: #2b2b2b;
    --card-white: #ffffff;
    --card-black: #060606;
    --ink: #111111;
    --frame: #1a1a1a;
    --paper-text: #f2f2f2;
    --photo-light: #e6e6e6;
    --photo-mid: #b9ad93;
    --photo-dark: #1e2433;
    --scene-dark: #0b0c0d;
    --scene-mid: #1b1d1c;
    --icon-green: #2f8f3a;
    --icon-red: #c4282d;
    --icon-blue: #2f4fa8;
    --icon-gold: #d49a2a;
  }
  * { margin: 0; padding: 0; box-sizing: border-box; }
  html, body { width: 1200px; height: 900px; overflow: hidden; }
  body {
    background: var(--stage);
    font-family: "Tinos", "Times New Roman", serif;
    position: relative;
  }
  .card {
    position: absolute;
    left: 320px;
    width: 560px;
    height: 320px;
    overflow: hidden;
  }

  /* Front */
  .card-front { top: 100px; background: var(--card-white); }
  .card-front .frame {
    position: absolute; inset: 14px;
    border: 2px solid var(--frame);
  }
  .portrait {
    position: absolute; left: 50px; bottom: 16px;
    width: 225px; height: 190px;
    background: linear-gradient(160deg, var(--photo-light) 0%, var(--photo-mid) 55%, var(--photo-dark) 100%);
  }
  .contact {
    position: absolute; right: 32px; top: 26px;
    text-align: right; color: var(--ink);
  }
  .company-mark {
    display: flex; align-items: center; justify-content: flex-end; gap: 6px;
    font-size: 13px; font-variant: small-caps; letter-spacing: 0.5px;
    margin-bottom: 10px;
  }
  .company-mark .dot { width: 10px; height: 10px; background: var(--ink); }
  .person-name {
    font-size: 28px; font-weight: 700; font-variant: small-caps; letter-spacing: 1px;
    line-height: 1;
  }
  .person-title {
    font-size: 17px; font-variant: small-caps; letter-spacing: 1px;
    margin-bottom: 12px;
  }
  .line {
    font-size: 13px; line-height: 1.4;
    display: flex; align-items: center; justify-content: flex-end; gap: 6px;
  }
  .line svg { width: 11px; height: 11px; flex: none; }

  /* Back */
  .card-back { top: 460px; background: var(--card-black); }
  .scene {
    position: absolute; inset: 0;
    background: radial-gradient(ellipse at 30% 65%, var(--scene-mid) 0%, var(--scene-dark) 55%, var(--card-black) 100%);
  }
  .brand {
    position: absolute; left: 0; right: 0; top: 150px;
    text-align: center; color: var(--paper-text);
  }
  .brand-name {
    display: inline-flex; align-items: center; gap: 12px;
    font-size: 34px; font-variant: small-caps; letter-spacing: 1px;
  }
  .brand-name .dot { width: 18px; height: 18px; background: var(--paper-text); }
  .brand-web {
    font-size: 15px; letter-spacing: 2px; margin-top: 6px;
  }
</style>
</head>
<body>

  <section class="card card-front">
    <div class="frame"></div>
    <div class="portrait" role="img" aria-label="Portrait photo of Marlon Tevaki in a light jacket"></div>
    <div class="contact">
      <div class="company-mark"><span class="dot"></span><span>Grey Heron Estates Inc</span></div>
      <div class="person-name">Marlon Tevaki</div>
      <div class="person-title">Vice President</div>
      <div class="line">604-512-3047
        <svg viewBox="0 0 12 12"><rect width="12" height="12" rx="2" fill="var(--icon-green)"/><path d="M3 3h2l1 2-1 1a5 5 0 0 0 2 2l1-1 2 1v2a7 7 0 0 1-7-7z" fill="#fff"/></svg>
      </div>
      <div class="line">604-488-1630
        <svg viewBox="0 0 12 12"><rect width="12" height="12" rx="2" fill="var(--icon-red)"/><rect x="3" y="4" width="6" height="5" fill="#fff"/></svg>
      </div>
      <div class="line">marlontevaki@mailbox-example.com
        <svg viewBox="0 0 12 12"><rect width="12" height="12" rx="2" fill="var(--icon-blue)"/><path d="M2 3.5h8v5H2z M2 3.5l4 3 4-3" fill="none" stroke="#fff" stroke-width="1"/></svg>
      </div>
      <div class="line">www.marlontevaki-example.com
        <svg viewBox="0 0 12 12"><circle cx="6" cy="6" r="6" fill="var(--icon-gold)"/><circle cx="6" cy="6" r="3" fill="none" stroke="#fff" stroke-width="1"/></svg>
      </div>
    </div>
  </section>

  <section class="card card-back">
    <div class="scene" role="img" aria-label="Dark evening photo of a waterfront home among trees"></div>
    <div class="brand">
      <div class="brand-name"><span class="dot"></span><span>Grey Heron Estates Inc</span></div>
      <div class="brand-web">www.greyheronestates-example.com</div>
    </div>
  </section>

</body>
</html>
```